Business Card Design

I need a design/ business card for a new company that caters for Event Hire (decorations and linen only) I am dabbling in rustic/ vintage designs for weddings and would like an elegant look to the cards. Something that will catch peoples eyes amongst the rest of the competitions cards and stand out to all fields, corporate/ weddings and general functions.

I am unsure of colours or pictures i would like so i am open to anything but possibly stick away from photos as i they are not more work of art on the card?

Target Market(s)

weddings and corporate events

Industry/Entity Type

Business

Contact Information for Business Card

Marlowe Weddings & Event Hire

Servicing the Harrowfield Region for Weddings, Corporate & Private Functions

marloweweddings@postvane.com
Phone: 0427 813 542

Requirements
Must have
• The writing "Marlowe Weddings & Event Hire" please
Nice to have
• Something that really stands out as a must have at your event
Should not have
• Pictures that are not of my work

```html
<!DOCTYPE html>
<html lang="en">
<head>
<meta charset="utf-8">
<title>Marlowe Weddings &amp; Event Hire – Business Card</title>
<link rel="stylesheet" href="https://fonts.googleapis.com/css2?family=Didact+Gothic&display=swap">
<style>
  :root {
    --page: #e9e7e4;
    --card-white: #fffdf8;
    --gold: #e7b21f;
    --gold-deep: #c98f12;
    --gold-pale: #f6e3a8;
    --ink: #221b12;
    --text: #111111;
  }
  * { box-sizing: border-box; margin: 0; padding: 0; }
  html, body { width: 1200px; height: 848px; overflow: hidden; }
  body {
    background: var(--page);
    font-family: "Didact Gothic", "Century Gothic", sans-serif;
    position: relative;
  }
  .card {
    position: absolute;
    top: 305px;
    width: 424px;
    height: 259px;
    background: var(--card-white);
    overflow: hidden;
    box-shadow: 0 2px 6px rgba(0,0,0,.18);
  }
  .card--front { left: 141px; }
  .card--back { left: 640px; }

  .brush-band {
    position: absolute;
    left: 0; right: 0;
    background:
      linear-gradient(100deg, rgba(255,255,255,0) 0%, rgba(255,240,190,.35) 30%, rgba(0,0,0,0) 55%, rgba(150,90,0,.25) 80%, rgba(255,230,160,.2) 100%),
      linear-gradient(180deg, var(--gold) 0%, var(--gold-deep) 100%);
  }
  .brush-band--top { top: 0; height: 42px; }
  .brush-band--bottom { bottom: 0; height: 47px; }
  .wash {
    position: absolute;
    left: 0; right: 0; top: 42px; bottom: 47px;
    background: linear-gradient(110deg, rgba(246,227,168,0) 0%, rgba(246,227,168,.35) 35%, rgba(255,253,248,0) 65%, rgba(246,227,168,.3) 100%);
  }

  .brand-name {
    position: absolute;
    left: 0; right: 0;
    text-align: center;
    color: var(--ink);
    font-weight: 400;
    line-height: 1;
    white-space: nowrap;
  }
  .card--front .brand-name {
    top: 53px;
    font-size: 80px;
    letter-spacing: 2px;
  }
  .tagline {
    position: absolute;
    left: 0; right: 0; top: 167px;
    text-align: center;
    color: var(--gold);
    font-size: 28px;
    line-height: 1;
    letter-spacing: 1px;
    white-space: nowrap;
  }

  .card--back .brand-name {
    top: 15px;
    font-size: 40px;
    letter-spacing: 2px;
  }
  .service-line {
    position: absolute;
    left: 0; right: 0; top: 80px;
    text-align: center;
    color: var(--text);
    font-size: 18px;
    line-height: 23px;
    letter-spacing: .3px;
    white-space: nowrap;
  }
  .contact-row {
    position: absolute;
    left: 0; right: 0;
    text-align: center;
    font-size: 17.5px;
    line-height: 20px;
    color: var(--text);
    letter-spacing: .3px;
    white-space: nowrap;
  }
  .contact-row--phone { top: 141px; }
  .contact-row--email { top: 166px; }
  .contact-label { color: var(--gold); margin-right: 4px; }
  .rule { position: absolute; }
  .rule--phone {
    top: 145px; left: 0; right: 0; height: 13px;
    background: linear-gradient(90deg, var(--gold) 0%, var(--gold-pale) 45%, rgba(255,255,255,0) 50%, var(--gold-pale) 55%, var(--gold) 100%);
    opacity: .55;
  }
  .rule--email {
    top: 181px; left: 0; right: 0; height: 1px;
    background: var(--gold-deep); opacity: .5;
  }
  .text-bg { background: var(--card-white); padding: 0 8px; }
</style>
</head>
<body>
  <section class="card card--front">
    <div class="brush-band brush-band--top" role="img" aria-label="Gold painted brush-stroke texture"></div>
    <div class="wash" role="img" aria-label="Faint gold brush wash"></div>
    <div class="brush-band brush-band--bottom" role="img" aria-label="Gold painted brush-stroke texture"></div>
    <h1 class="brand-name">MARLOWE</h1>
    <p class="tagline">WEDDINGS &amp; EVENT HIRE</p>
  </section>

  <section class="card card--back">
    <div class="brush-band brush-band--top" role="img" aria-label="Gold painted brush-stroke texture"></div>
    <div class="wash" role="img" aria-label="Faint gold brush wash"></div>
    <div class="brush-band brush-band--bottom" role="img" aria-label="Gold painted brush-stroke texture"></div>
    <h2 class="brand-name">MARLOWE</h2>
    <p class="service-line">Servicing the Harrowfield Region for<br>Weddings, Corporate &amp; Private Functions</p>
    <div class="rule rule--phone"></div>
    <div class="rule rule--email"></div>
    <p class="contact-row contact-row--phone"><span class="text-bg"><span class="contact-label">P</span>0427 813 542</span></p>
    <p class="contact-row contact-row--email"><span class="text-bg"><span class="contact-label">E</span>marloweweddings@postvane.com</span></p>
  </section>
</body>
</html>
```